Business Card Design for Occupational Medicine Start Up Company

We need to design a professional business card. We are a healthcare company providing occupational medicine services to blue collar industries. We are professional, efficient and high quality service providers.

Target Market(s)

Blue Collar Industry: Shipbuilding, Ports, Trucking Companies; The Executives and Safety Officers for these companies

Industry/Entity Type

Healthcare

Contact Information for Business Card

Logo, Name, Title, Email, Phone

Other font styles liked:
• Please match our Brand Guide

Requirements
Must have
• Our Company Colors and Logo

```html
<!DOCTYPE html>
<html lang="en">
<head>
<meta charset="utf-8">
<title>Crewline Health — Business Card</title>
<link rel="stylesheet" href="https://fonts.googleapis.com/css2?family=Montserrat:wght@400;600;700&display=swap">
<style>
  :root {
    --navy: #2b3480;
    --sky: #22a2dc;
    --amber: #f6ac48;
    --white: #ffffff;
    --paper: #f7f7f7;
    --mist: #dedede;
    --page: #ffffff;
  }
  * { box-sizing: border-box; margin: 0; padding: 0; }
  html, body { width: 687px; height: 1200px; overflow: hidden; background: var(--page); }
  body { font-family: "Montserrat", sans-serif; position: relative; }

  .card {
    position: absolute;
    left: 63px;
    width: 560px;
    height: 320px;
    overflow: hidden;
    box-shadow: 0 2px 8px rgba(0,0,0,.18);
  }
  .card-front { top: 240px; background: var(--white); }
  .card-back { top: 640px; background: var(--navy); }
  .card svg.shapes { position: absolute; inset: 0; }

  /* front */
  .faint-mark {
    position: absolute; left: 0; top: 28px; width: 150px; height: 150px;
    background: radial-gradient(circle at 40% 45%, var(--mist) 0%, rgba(222,222,222,.4) 55%, rgba(255,255,255,0) 72%);
  }
  .brand {
    position: absolute; left: 215px; top: 150px; width: 320px;
    display: flex; align-items: center; justify-content: center; gap: 10px;
  }
  .brand-dot { width: 18px; height: 18px; border-radius: 50%; background: var(--navy); }
  .brand-name { font-weight: 700; font-size: 27px; color: var(--navy); letter-spacing: .5px; }
  .front-url {
    position: absolute; left: 215px; top: 252px; width: 320px; text-align: center;
    font-weight: 600; font-size: 15px; color: var(--navy); letter-spacing: .6px;
  }
  .front-url .accent { color: var(--sky); }

  /* back */
  .holder { position: absolute; left: 30px; top: 70px; width: 180px; }
  .holder-name { font-weight: 700; font-size: 22px; color: var(--white); line-height: 1; white-space: nowrap; }
  .holder-title { font-weight: 700; font-size: 10px; color: var(--amber); margin-top: 4px; padding-bottom: 4px; border-bottom: 1.5px solid var(--white); }
  .contacts { position: absolute; left: 30px; top: 152px; list-style: none; }
  .contacts li { display: flex; align-items: flex-start; gap: 10px; color: var(--white); font-weight: 600; font-size: 12px; line-height: 17px; margin-bottom: 11px; }
  .contacts svg { width: 14px; height: 14px; flex: none; margin-top: 1px; fill: var(--sky); }
  .contacts .accent { color: var(--amber); }
  .back-pattern { position: absolute; left: 300px; top: 0; width: 260px; height: 130px;
    background: linear-gradient(160deg, var(--paper), rgba(247,247,247,0)); }
  .back-brand {
    position: absolute; left: 325px; top: 128px; width: 220px;
    display: flex; flex-direction: column; align-items: center; gap: 8px;
  }
  .back-brand .brand-dot { width: 26px; height: 26px; }
  .back-brand .brand-name { font-size: 24px; text-align: center; line-height: 1.15; }
</style>
</head>
<body>

<section class="card card-front" aria-label="Card front">
  <div class="faint-mark" role="img" aria-label="Faint oversized brand symbol decoration"></div>
  <svg class="shapes" viewBox="0 0 560 320" aria-hidden="true">
    <path d="M0,60 Q150,300 390,320 L0,320 Z" fill="var(--amber)"/>
    <path d="M0,70 Q150,304 380,320 L0,320 Z" fill="var(--navy)"/>
    <path d="M330,320 Q480,318 560,288 L560,320 Z" fill="var(--sky)"/>
  </svg>
  <div class="brand">
    <span class="brand-dot"></span>
    <span class="brand-name">CREWLINE HEALTH</span>
  </div>
  <p class="front-url">www.<span class="accent">crewlinehealth</span>.com</p>
</section>

<section class="card card-back" aria-label="Card back">
  <svg class="shapes" viewBox="0 0 560 320" aria-hidden="true">
    <path d="M266,0 Q192,180 418,320 L560,320 L560,0 Z" fill="var(--sky)"/>
    <path d="M277,0 Q204,180 432,320 L560,320 L560,0 Z" fill="var(--amber)"/>
    <path d="M287,0 Q214,180 446,320 L560,320 L560,0 Z" fill="var(--white)"/>
  </svg>
  <div class="back-pattern" role="img" aria-label="Light repeating brand symbol pattern"></div>

  <div class="holder">
    <h1 class="holder-name">DANA HOLLOWAY</h1>
    <p class="holder-title">CHIEF EXECUTIVE OFFICER</p>
  </div>

  <ul class="contacts">
    <li>
      <svg viewBox="0 0 24 24"><path d="M6.6 10.8a15 15 0 0 0 6.6 6.6l2.2-2.2c.3-.3.7-.4 1-.2 1.1.4 2.3.6 3.6.6.6 0 1 .4 1 1V20c0 .6-.4 1-1 1A17 17 0 0 1 3 4c0-.6.4-1 1-1h3.5c.6 0 1 .4 1 1 0 1.3.2 2.5.6 3.6.1.3 0 .7-.2 1z"/></svg>
      +1 (555) 014-2290
    </li>
    <li>
      <svg viewBox="0 0 24 24"><path d="M2 5h20v14H2z" /><path d="M2 5l10 8 10-8" fill="none" stroke="#2b3480" stroke-width="1.6"/></svg>
      hello@crewlinehealth.com
    </li>
    <li>
      <svg viewBox="0 0 24 24"><path d="M12 2a7 7 0 0 0-7 7c0 5 7 13 7 13s7-8 7-13a7 7 0 0 0-7-7zm0 9.5A2.5 2.5 0 1 1 12 6.5a2.5 2.5 0 0 1 0 5z"/></svg>
      <span>Harbor Row 418, 5th Floor<br>Norfolk - United States</span>
    </li>
    <li>
      <svg viewBox="0 0 24 24"><circle cx="12" cy="12" r="10"/><path d="M2 12h20M12 2c3 3 3 17 0 20M12 2c-3 3-3 17 0 20" fill="none" stroke="#2b3480" stroke-width="1.3"/></svg>
      <span>www.<span class="accent">crewlinehealth</span>.com</span>
    </li>
  </ul>

  <div class="back-brand">
    <span class="brand-dot"></span>
    <span class="brand-name">CREWLINE<br>HEALTH</span>
  </div>
</section>

</body>
</html>
```